I need a business card design for a Boutique Pilates studio.

I would like to see designs similar to the one that I have uploaded.
thinking between two slogans:
'No ordinary place'
'Not so ordinary'

Contact Information for Business Card

KiVa Pilates

```html
<!DOCTYPE html>
<html lang="en">
<head>
<meta charset="UTF-8">
<title>KiVa Pilates – Business Card</title>
<link href="https://fonts.googleapis.com/css2?family=Oswald:wght@600&family=Arimo:wght@400&display=swap" rel="stylesheet">
<style>
  :root {
    --stage: #1b1b1b;
    --card: #2f2f2f;
    --edge: #f2d300;
    --accent: #f5d800;
    --ink: #ffffff;
    --ink-soft: #e6e6e6;
    --emboss: #252525;
    --emboss-light: #3a3a3a;
    --rule: #8a8a8a;
  }
  * { margin: 0; padding: 0; box-sizing: border-box; }
  html, body {
    width: 1200px; height: 874px; overflow: hidden;
    background: var(--stage);
  }
  .stage {
    position: relative; width: 1200px; height: 874px;
    display: flex; flex-direction: column; align-items: center; justify-content: center;
    gap: 44px;
  }
  .card {
    position: relative; width: 600px; height: 343px;
    background: var(--card);
    border-radius: 22px;
    box-shadow: 0 3px 0 var(--edge);
    overflow: hidden;
  }

  /* Front face: blind-embossed name */
  .front .brand {
    position: absolute; left: 0; right: 0; top: 0; bottom: 0;
    display: flex; align-items: center; justify-content: center;
    font-family: "Arimo", Arial, sans-serif;
    font-size: 52px; letter-spacing: 1px;
    color: var(--emboss);
    text-shadow: 0 1px 0 var(--emboss-light);
  }

  /* Back face */
  .back .brand {
    position: absolute; left: 0; width: 306px; top: 0; bottom: 0;
    display: flex; align-items: center; justify-content: center;
    font-family: "Arimo", Arial, sans-serif;
    font-size: 34px; color: var(--accent);
  }
  .back .divider {
    position: absolute; left: 306px; top: 40px; width: 1.5px; height: 260px;
    background: linear-gradient(to bottom, transparent, var(--rule) 30%, var(--rule) 70%, transparent);
  }
  .contact {
    position: absolute; left: 330px; top: 58px; right: 20px;
    font-family: "Arimo", Arial, sans-serif; color: var(--ink);
  }
  .contact .name {
    font-family: "Oswald", sans-serif; font-weight: 600;
    font-size: 25px; color: var(--accent); line-height: 1.1;
  }
  .contact .role { font-size: 14px; color: var(--ink-soft); margin-top: 2px; }
  .contact .address { font-size: 15px; line-height: 1.3; margin-top: 20px; }
  .contact .lines { list-style: none; margin-top: 16px; }
  .contact .lines li {
    display: flex; align-items: center; gap: 12px;
    font-size: 15px; line-height: 1.3;
  }
  .contact .lines svg { width: 13px; height: 13px; flex: none; fill: var(--accent); }
</style>
</head>
<body>
<main class="stage">
  <section class="card front" aria-label="Card front">
    <div class="brand">KiVa Pilates</div>
  </section>

  <section class="card back" aria-label="Card back">
    <div class="brand">KiVa Pilates</div>
    <div class="divider"></div>
    <div class="contact">
      <div class="name">CLARA WESTON</div>
      <div class="role">President</div>
      <div class="address">412 Larchwood Drive<br>Fernvale, Canada 52816</div>
      <ul class="lines">
        <li>
          <svg viewBox="0 0 24 24" aria-hidden="true"><path d="M6.6 10.8a15 15 0 0 0 6.6 6.6l2.2-2.2a1 1 0 0 1 1-.25 11.4 11.4 0 0 0 3.6.57 1 1 0 0 1 1 1V20a1 1 0 0 1-1 1A17 17 0 0 1 3 4a1 1 0 0 1 1-1h3.5a1 1 0 0 1 1 1c0 1.250.2 2.450.57 3.570a1 1 0 0 1-.25 1z"/></svg>
          555-210-4417
        </li>
        <li>
          <svg viewBox="0 0 24 24" aria-hidden="true"><path d="M7 1h10a2 2 0 0 1 2 2v18a2 2 0 0 1-2 2H7a2 2 0 0 1-2-2V3a2 2 0 0 1 2-2zm0 3v14h10V4z"/></svg>
          555-382-9061
        </li>
        <li>
          <svg viewBox="0 0 24 24" aria-hidden="true"><path d="M2 5h20v14H2zm2 2v.5l8 5 8-5V7l-8 5z"/></svg>
          info@kivapilates.com
        </li>
        <li>
          <svg viewBox="0 0 24 24" aria-hidden="true"><path d="M12 2a10 10 0 1 0 0 20 10 10 0 0 0 0-20zm-1 17.9A8 8 0 0 1 4 12l5 5v1a2 2 0 0 0 2 2zm6.9-2.5A2 2 0 0 0 16 16h-1v-3a1 1 0 0 0-1-1H8v-2h2a1 1 0 0 0 1-1V7h2a2 2 0 0 0 2-2v-.4a8 8 0 0 1 2.9 12.8z"/></svg>
          www.kivapilates.com
        </li>
      </ul>
    </div>
  </section>
</main>
</body>
</html>
```